Corporate business card

Business card design for IT consultancy company.
Clients are larger companies.
Card should have round edges on some or all.
Make the user stop and look at the card.
Steel grey background. But if you have a better idea, show me.
Target Market(s)
Corporate - a but web 2.0
Industry/Entity Type
Business
Contact Information for Business Card
As per design.
Font styles to use
Other font styles liked:
- Helvetica
Colors
5c5c5c
ec2027
ffffff
Requirements
Must have
- Clean design - follow vorla styles
- text in white
- Lets have a conversation in red
- Powered by passion in red
Nice to have
- Uncluttered
Should not have
- Cluttered

```html
<!DOCTYPE html>
<html lang="en">
<head>
<meta charset="utf-8">
<title>Kestrel Advisory — Business Card</title>
<link href="https://fonts.googleapis.com/css2?family=Roboto+Condensed:ital,wght@0,400;0,700;1,400&family=Arimo:wght@400;700&display=swap" rel="stylesheet">
<style>
  :root {
    --page-bg: #fdf0fd;
    --card-steel: #acacac;
    --brand-red: #b3141b;
    --accent-red: #9c1015;
    --ink-dark: #4a4a4a;
    --ink-white: #ffffff;
  }
  * { margin: 0; padding: 0; box-sizing: border-box; }
  html, body {
    width: 1200px; height: 510px; overflow: hidden;
    background: var(--page-bg);
    font-family: "Arimo", Helvetica, Arial, sans-serif;
  }
  .canvas { position: relative; width: 1200px; height: 510px; }

  .card {
    position: absolute;
    width: 389px; height: 237px;
    background: var(--card-steel);
  }
  .card--front { left: 200px; top: 136px; border-bottom-right-radius: 28px; }
  .card--back  { left: 612px; top: 137px; border-bottom-left-radius: 28px; height: 236px; }

  /* Front */
  .front-brand {
    position: absolute; left: 0; right: 0; top: 76px;
    display: flex; justify-content: center; align-items: center; gap: 10px;
    color: var(--brand-red);
    font-family: "Roboto Condensed", "Arial Narrow", sans-serif;
    font-weight: 700; font-size: 38px; letter-spacing: 1px; line-height: 1;
    text-transform: uppercase;
  }
  .front-brand .brand-square {
    width: 18px; height: 18px; background: var(--brand-red);
  }
  .front-brand small {
    display: block; font-size: 38px;
  }
  .front-rule {
    position: absolute; left: 51px; width: 274px; top: 158px;
    height: 1px; background: var(--accent-red);
  }
  .front-tagline {
    position: absolute; left: 0; right: 0; top: 170px;
    text-align: center; color: var(--accent-red);
    font-size: 13px; font-style: italic; letter-spacing: 0.2px;
  }

  /* Back */
  .back-brand {
    position: absolute; left: 42px; top: 41px;
    display: flex; align-items: center; gap: 5px;
    color: var(--brand-red);
    font-family: "Roboto Condensed", "Arial Narrow", sans-serif;
    font-weight: 700; font-size: 15px; line-height: 1.05;
    text-transform: uppercase;
  }
  .back-brand .brand-square { width: 8px; height: 8px; background: var(--brand-red); }

  .holder {
    position: absolute; left: 148px; top: 40px;
    font-family: "Roboto Condensed", "Arial Narrow", sans-serif;
    color: var(--ink-dark); line-height: 1.3;
  }
  .holder__name { font-weight: 700; font-size: 16px; letter-spacing: 0.3px; }
  .holder__role { font-weight: 400; font-size: 16px; }

  .contacts {
    position: absolute; left: 112px; top: 99px;
    list-style: none;
  }
  .contacts li {
    display: flex; align-items: center; height: 17.4px;
    color: var(--ink-white); font-size: 12px; letter-spacing: 1px;
  }
  .contacts svg { width: 12px; height: 12px; margin-right: 19px; flex: none; }
  .contacts .spaced { letter-spacing: 3.4px; }

  .cta {
    position: absolute; left: 115px; top: 197px;
    color: var(--accent-red);
    font-family: "Roboto Condensed", "Arial Narrow", sans-serif;
    font-size: 15px; letter-spacing: 0.3px;
  }
</style>
</head>
<body>
<main class="canvas">

  <section class="card card--front" aria-label="Card front">
    <div class="front-brand">
      <span class="brand-square" aria-hidden="true"></span>
      <span>Kestrel Advisory</span>
    </div>
    <div class="front-rule"></div>
    <p class="front-tagline">POWERED BY PASSION !</p>
  </section>

  <section class="card card--back" aria-label="Card back">
    <div class="back-brand">
      <span class="brand-square" aria-hidden="true"></span>
      <span>Kestrel<br>Advisory</span>
    </div>

    <div class="holder">
      <p class="holder__name">DANE HOLLOWAY</p>
      <p class="holder__role">MANAGING PARTNER</p>
    </div>

    <ul class="contacts">
      <li>
        <svg viewBox="0 0 12 12" aria-hidden="true"><path d="M1 6 L6 1.5 L11 6 M2.5 5 V10.5 H9.5 V5" fill="none" stroke="#9c1015" stroke-width="1.4"/></svg>
        +61390004417
      </li>
      <li>
        <svg viewBox="0 0 12 12" aria-hidden="true"><rect x="3.5" y="1" width="5" height="10" rx="0.8" fill="none" stroke="#9c1015" stroke-width="1.4"/><line x1="3.5" y1="8.5" x2="8.5" y2="8.5" stroke="#9c1015" stroke-width="1"/></svg>
        <span class="spaced">0412558904</span>
      </li>
      <li>
        <svg viewBox="0 0 12 12" aria-hidden="true"><rect x="2" y="2" width="8" height="8" fill="none" stroke="#9c1015" stroke-width="1.4"/><circle cx="6" cy="6" r="1.5" fill="#9c1015"/></svg>
        DANE_HOLLOWAY
      </li>
      <li>
        <svg viewBox="0 0 12 12" aria-hidden="true"><rect x="2" y="2" width="8" height="8" fill="none" stroke="#9c1015" stroke-width="1.4"/><line x1="4" y1="6" x2="8" y2="6" stroke="#9c1015" stroke-width="1.2"/></svg>
        WWW.KESTRELADVISORY.COM.AU
      </li>
      <li>
        <svg viewBox="0 0 12 12" aria-hidden="true"><rect x="1" y="3" width="10" height="6.5" fill="none" stroke="#9c1015" stroke-width="1.4"/><path d="M1 3 L6 7 L11 3" fill="none" stroke="#9c1015" stroke-width="1.2"/></svg>
        DANE@KESTRELADVISORY.COM.AU
      </li>
    </ul>

    <p class="cta">LET’S HAVE A CONVERSATION !</p>
  </section>

</main>
</body>
</html>
```